WordPress Site Design and Code for Technology Consulting Startup

We need a WordPress design and code to a new site on Tallow Bay. We have the logo and colors ready. The site will be a brochure site with a CONTACT page that contains a form that the prospective client fills out. The other pages would be ABOUT / SERVICES (3 option drop-down) / SUPPORT. The site should be appropriate for an IT Consulting / IT Managed Services / IT Project Management services in the Chicago area.

Across small, medium, large businesses.

Technology, network infrastructure, IT.

Coded - Design and coding required

5+ page

• I prefer mid-modern / simple / art deco / minimalist.

```html
<!DOCTYPE html>
<html lang="en">
<head>
<meta charset="utf-8">
<title>Corvane — Technology Consulting</title>
<link href="https://fonts.googleapis.com/css2?family=Orbitron:wght@700;800&family=Open+Sans:wght@400;600;700&display=swap" rel="stylesheet">
<style>
:root{
  --orange:#e97e14;
  --teal:#2a93ab;
  --teal-deep:#1f7d95;
  --navy:#0c2a45;
  --navy-deep:#071a2e;
  --ink:#111;
  --text:#555;
  --white:#fff;
  --footer:#05090e;
  --field:#fff;
}
*{margin:0;padding:0;box-sizing:border-box}
html,body{width:1200px;height:2977px;overflow:hidden;background:var(--white)}
body{position:relative;font-family:"Open Sans",Arial,sans-serif;color:var(--text)}
.abs{position:absolute}
.display{font-family:"Orbitron","Arial Black",sans-serif;font-weight:800;letter-spacing:1px;text-transform:uppercase}
.btn{position:absolute;background:var(--orange);color:var(--white);font-weight:700;text-transform:uppercase;display:flex;align-items:center;justify-content:center;letter-spacing:.3px}

/* hero */
.hero-bg{position:absolute;left:0;top:0;width:1200px;height:712px}
.brand{position:absolute;color:var(--white);font-weight:700;display:flex;align-items:center;gap:10px}
.brand .mark{width:14px;height:14px;background:var(--orange)}
.nav{position:absolute;top:52px;left:407px;display:flex;color:var(--white);font-weight:700;font-size:19px}
.nav span{position:absolute;white-space:nowrap}
.hero-title{left:111px;top:250px;font-size:56px;line-height:56px;color:var(--white)}
.hero-copy{left:111px;top:376px;width:440px;font-size:16px;line-height:25.5px;color:var(--white)}
.scroll-cue{left:577px;top:668px;width:46px;height:66px;border-radius:23px;background:var(--white);box-shadow:0 3px 10px rgba(0,0,0,.2);display:flex;align-items:center;justify-content:center}

/* about */
.about-brand{left:136px;top:840px;width:406px;height:348px;display:flex;align-items:center;justify-content:center;gap:16px;font-size:64px;font-weight:700;color:var(--teal)}
.about-brand .mark{width:40px;height:40px;background:var(--orange)}
.section-title{font-size:38px;color:var(--ink)}
.about-copy{left:632px;top:870px;width:436px;font-size:14.6px;line-height:24.9px}

/* services */
.services{left:0;top:1325px;width:1200px;height:594px}
.services-sub{left:150px;top:1446px;width:900px;text-align:center;color:var(--white);font-size:16px;line-height:25px}
.service{position:absolute;top:1546px;width:330px;text-align:center;color:var(--white)}
.service .icon{width:106px;height:106px;border-radius:50%;background:var(--white);margin:0 auto;border:6px solid #d7dde0;display:flex;align-items:center;justify-content:center}
.service h3{margin-top:20px;font-size:19.5px;font-family:"Orbitron","Arial Black",sans-serif;font-weight:800;text-transform:uppercase;white-space:nowrap}
.service p{margin-top:10px;font-size:15px;line-height:25px;padding:0 20px}
.service a{display:inline-block;margin-top:7px;color:var(--white);font-weight:700;font-size:16px;text-decoration:underline}

/* contact */
.info{position:absolute;left:123px;display:flex;gap:14px}
.info .ring{width:50px;height:50px;border-radius:50%;border:2px solid var(--orange);display:flex;align-items:center;justify-content:center;flex:none}
.info h4{font-weight:400;color:#222;font-size:19px;line-height:24px;margin-top:-2px}
.info p{font-size:16px;line-height:26px;color:#666}
.field{position:absolute;background:var(--field);box-shadow:0 2px 14px rgba(0,0,0,.08);color:#777;font-size:16px;padding:14px 24px}

/* support */
.footer{left:0;top:2547px;width:1200px;height:430px;background:radial-gradient(ellipse at 60% 30%,#10202e 0%,var(--footer) 70%)}
.support-card{left:0;top:2430px;width:934px;height:199px;background:var(--white);box-shadow:0 4px 16px rgba(0,0,0,.06)}
.support-copy{left:111px;top:2517px;width:500px;font-size:14.4px;line-height:23.5px}
.footer-brand{left:300px;top:2715px;width:600px;justify-content:center;font-size:58px}
.footer-brand .mark{width:22px;height:22px}
.footer-nav{position:absolute;top:2856px;color:var(--white);font-size:19px}
.copyright{left:0;top:2922px;width:1200px;text-align:center;color:var(--white);font-size:14px}
</style>
</head>
<body>

<svg class="hero-bg" viewBox="0 0 1200 712" role="img" aria-label="Dark blue photograph of a hand touching a tablet with glowing growth charts and data rings">
  <defs>
    <linearGradient id="heroGrad" x1="0" y1="0" x2="1" y2="0.4">
      <stop offset="0" stop-color="#12304a"/>
      <stop offset="0.45" stop-color="#0d3654"/>
      <stop offset="0.75" stop-color="#1a7ea0"/>
      <stop offset="1" stop-color="#0f4f72"/>
    </linearGradient>
  </defs>
  <polygon points="0,0 1200,0 1200,636 1006,636 600,712 194,636 0,636" fill="url(#heroGrad)"/>
</svg>

<div class="brand" style="left:111px;top:44px;font-size:30px"><span class="mark"></span>Corvane</div>

<nav class="nav">
  <span style="left:0">HOME</span>
  <span style="left:106px">ABOUT US</span>
  <span style="left:251px">SERVICES</span>
  <span style="left:385px">SUPPORT</span>
</nav>
<div class="btn" style="left:922px;top:43px;width:166px;height:44px;font-size:19px">Contact Us</div>

<h1 class="abs display hero-title">Welcome to<br>Corvane</h1>
<p class="abs hero-copy">Lorem Ipsum is simply dummy text of the printing and typesetting industry. Lorem Ipsum has been the industry's standard dummy text ever since the</p>
<div class="btn" style="left:111px;top:483px;width:166px;height:44px;font-size:18px">Get Started</div>

<div class="abs scroll-cue">
  <svg width="30" height="30" viewBox="0 0 30 30" aria-hidden="true">
    <circle cx="15" cy="15" r="12" fill="none" stroke="#e97e14" stroke-width="2.2"/>
    <path d="M15 8v13M10 16l5 5 5-5" fill="none" stroke="#e97e14" stroke-width="2.2" stroke-linecap="round" stroke-linejoin="round"/>
  </svg>
</div>

<div class="abs about-brand"><span class="mark"></span>Corvane</div>
<h2 class="abs display section-title" style="left:632px;top:812px">About Us</h2>
<p class="abs about-copy">There are many variations of passages of Lorem Ipsum available, but the majority have suffered alteration in some form, by injected humour, or randomised words which don't look even slightly believable. If you are going to use a passage of Lorem Ipsum, you need to be sure there isn't anything embarrassing hidden in the middle of text. All the Lorem Ipsum generators on the Internet tend to repeat predefined chunks as necessary, making this the first true generator on the Internet. It uses a dictionary of over 200 Latin words, combined with a handful of model sentence structures, to generate Lorem Ipsum which looks reasonable.</p>
<div class="btn" style="left:632px;top:1168px;width:143px;height:41px;font-size:16.5px">Read More</div>

<div class="abs services" role="img" aria-label="Teal background photograph with faint security padlock and network icons" style="background:linear-gradient(135deg,#2f9bb3 0%,var(--teal) 50%,var(--teal-deep) 100%)"></div>
<h2 class="abs display section-title" style="left:0;top:1390px;width:1200px;text-align:center;color:var(--white)">Our Services</h2>
<p class="abs services-sub">The standard chunk of Lorem Ipsum used since the 1500s is reproduced below for those interested. Sections 1.10.32 and 1.10.33 from "de Finibus Bonorum et Malorum" by Cicero are also reproduced</p>

<div class="service" style="left:78px">
  <div class="icon"><svg width="44" height="44" viewBox="0 0 44 44" fill="none" stroke="#2a93ab" stroke-width="2"><path d="M4 30h8l8 3h10l8-6-3-2-8 4h-7"/><path d="M4 38h8l6 2h12l10-8"/><circle cx="24" cy="14" r="6"/><path d="M24 4v3M24 21v3M14 14h3M31 14h3"/></svg></div>
  <h3>IT Consulting</h3>
  <p>There are many variations of passages of Lorem Ipsum available, but the majority have suffered alteration in some form, by injected humour</p>
  <a href="#">Read More</a>
</div>
<div class="service" style="left:422px">
  <div class="icon"><svg width="44" height="44" viewBox="0 0 44 44" fill="none" stroke="#2a93ab" stroke-width="2"><circle cx="22" cy="14" r="7"/><circle cx="22" cy="14" r="3"/><path d="M8 38v-6a4 4 0 0 1 8 0v6M18 38v-8a4 4 0 0 1 8 0v8M28 38v-6a4 4 0 0 1 8 0v6M5 38h34"/></svg></div>
  <h3>IT Managed Services</h3>
  <p>There are many variations of passages of Lorem Ipsum available, but the majority have suffered alteration in some form, by injected humour</p>
  <a href="#">Read More</a>
</div>
<div class="service" style="left:776px">
  <div class="icon"><svg width="44" height="44" viewBox="0 0 44 44" fill="none" stroke="#2a93ab" stroke-width="2"><path d="M22 8a10 10 0 0 0-6 18v5h12v-5a10 10 0 0 0-6-18z"/><path d="M17 35h10M19 39h6M22 2v3M8 16H5M39 16h-3M11 6l2 2M33 6l-2 2"/></svg></div>
  <h3>Project Management</h3>
  <p>There are many variations of passages of Lorem Ipsum available, but the majority have suffered alteration in some form, by injected humour</p>
  <a href="#">Read More</a>
</div>

<h2 class="abs display section-title" style="left:0;top:2003px;width:1200px;text-align:center">Contact Us</h2>

<div class="info" style="top:2077px">
  <div class="ring"><svg width="18" height="20" viewBox="0 0 18 20"><path d="M9 1a7 7 0 0 0-7 7c0 5 7 11 7 11s7-6 7-11a7 7 0 0 0-7-7z" fill="#e97e14"/><circle cx="9" cy="8" r="2.5" fill="#fff"/></svg></div>
  <div><h4>Location</h4><p>14y, Corvane<br>Lorem ipsum dolor</p></div>
</div>
<div class="info" style="top:2181px">
  <div class="ring"><svg width="18" height="18" viewBox="0 0 24 24"><path d="M6.6 10.8a15 15 0 0 0 6.6 6.6l2.2-2.2a1 1 0 0 1 1-.25 11.4 11.4 0 0 0 3.6.6 1 1 0 0 1 1 1V20a1 1 0 0 1-1 1A17 17 0 0 1 3 4a1 1 0 0 1 1-1h3.5a1 1 0 0 1 1 1 11.4 11.4 0 0 0 .6 3.6 1 1 0 0 1-.25 1z" fill="#e97e14"/></svg></div>
  <div><h4>Phone</h4><p>+1 555 010 4821</p></div>
</div>
<div class="info" style="top:2277px">
  <div class="ring"><svg width="20" height="16" viewBox="0 0 20 16"><rect x="1" y="1" width="18" height="14" rx="2" fill="#e97e14"/><path d="M2 3l8 6 8-6" fill="none" stroke="#fff" stroke-width="1.6"/></svg></div>
  <div><h4>Email</h4><p>info@corvane.com</p></div>
</div>

<div class="field" style="left:446px;top:2076px;width:317px;height:51px">Name</div>
<div class="field" style="left:446px;top:2144px;width:317px;height:51px">Phone</div>
<div class="field" style="left:446px;top:2211px;width:317px;height:51px">Email</div>
<div class="btn" style="left:445px;top:2282px;width:318px;height:52px;font-size:16.5px">Submit Here</div>
<div class="field" style="left:784px;top:2076px;width:300px;height:257px">Type your message</div>

<div class="abs footer" role="img" aria-label="Dark background with faint network of connected dots"></div>
<div class="abs support-card"></div>
<h2 class="abs display section-title" style="left:111px;top:2467px;font-size:37px">Support</h2>
<p class="abs support-copy">Lorem Ipsum is simply dummy text of the printing and typesetting industry. Lorem Ipsum has been the industry's standard dummy text ever since the 1500s, when an unknown printer took</p>
<div class="btn" style="left:710px;top:2504px;width:169px;height:52px;font-size:17px">Join With Us</div>

<div class="brand footer-brand"><span class="mark"></span>Corvane</div>

<div class="footer-nav" style="left:170px">HOME</div>
<div class="footer-nav" style="left:276px">|</div>
<div class="footer-nav" style="left:334px">ABOUT US</div>
<div class="footer-nav" style="left:476px">|</div>
<div class="footer-nav" style="left:534px">SERVICES</div>
<div class="footer-nav" style="left:666px">|</div>
<div class="footer-nav" style="left:724px">SUPPORT</div>
<div class="footer-nav" style="left:858px">|</div>
<div class="footer-nav" style="left:916px">CONTACT US</div>

<p class="abs copyright">© COPYRIGHT 2023 CORVANE | ALL RIGHTS RESERVED</p>

</body>
</html>
```